KV HOLDING Business Cards

I need business cards for "KV Holding group LLC" doublesided... logo on the back (also include logo on front)
logo attached to project... i have jpg up..
Company Info:
418 East Marlow Avenue, Suite 7B
Chicago, Illinois 60617
facsimile 312-555-0188 (list fax, address, website on all cards.)
www.kvholdinggroup.example
Three different people on cards:
Dorian P. Kell, CPA MST
Principal
ofc 312-555-0142
mobile 312-555-0167
dorianpkell@kvholdinggroup.example
Marcus T. Brenholt, CPA MST
Principal
marcustbrenholt@kvholdinggroup.example
mobile 708-555-0119
ofc 312-555-0142
Nigel F Carrow
Principal
ofc 312-555-0142
no mobile
nigelfcarrow@kvholdinggroup.example
I have multiple projects listed.. see below:
Business cards for amber gate equity llc
letterhead
envelopes
Business cards for KV Holding LLC
letterhead
envelopes
Target Market(s)
rich people
Industry/Entity Type
Business
Look and feel

```html
<!DOCTYPE html>
<html lang="en">
<head>
<meta charset="utf-8">
<title>KV Holding Group LLC – Business Cards</title>
<link rel="stylesheet" href="https://fonts.googleapis.com/css2?family=Cinzel:wght@400&family=Ubuntu:wght@400;500&display=swap">
<style>
  :root {
    --navy: #123f73;
    --navy-deep: #0e3765;
    --paper: #ffffff;
    --ink: #262626;
    --rule: #8c8c8c;
    --stage: #e8e5e0;
    --logo-font: "Cinzel", serif;
    --text-font: "Ubuntu", sans-serif;
  }

  * { box-sizing: border-box; margin: 0; padding: 0; }

  html, body {
    width: 1200px;
    height: 750px;
    overflow: hidden;
  }

  body {
    background: var(--stage);
    position: relative;
    font-family: var(--text-font);
  }

  .card {
    position: absolute;
    top: 220px;
    width: 540px;
    height: 310px;
    box-shadow: 0 6px 18px rgba(0, 0, 0, 0.18);
    overflow: hidden;
  }

  /* ---------- Front ---------- */
  .card-front {
    left: 40px;
    background: var(--paper);
    color: var(--ink);
  }

  .front-wordmark {
    position: absolute;
    left: 24px;
    top: 96px;
    font-family: var(--logo-font);
    font-weight: 400;
    font-size: 23px;
    letter-spacing: 0.5px;
    color: var(--navy);
    white-space: nowrap;
  }

  .company-address {
    position: absolute;
    left: 330px;
    top: 34px;
    width: 190px;
    font-style: normal;
    font-size: 9.5px;
    line-height: 1.35;
    text-align: center;
  }

  .contact-divider {
    position: absolute;
    left: 24px;
    right: 20px;
    top: 142px;
    display: flex;
    align-items: center;
    gap: 10px;
  }

  .contact-divider .rule {
    height: 2px;
    background: var(--rule);
  }

  .contact-divider .rule-left { flex: 1; }
  .contact-divider .rule-right { width: 66px; }

  .contact-heading {
    font-size: 13px;
    font-weight: 500;
    color: var(--navy);
    white-space: nowrap;
  }

  .people {
    position: absolute;
    left: 10px;
    right: 10px;
    top: 176px;
    display: grid;
    grid-template-columns: repeat(3, 1fr);
    gap: 4px;
  }

  .person {
    font-size: 8.5px;
    line-height: 1.4;
    text-align: center;
    white-space: nowrap;
  }

  .website {
    position: absolute;
    left: 24px;
    top: 264px;
    font-size: 9px;
  }

  .website a {
    color: var(--navy);
    font-weight: 500;
    text-decoration: none;
  }

  .stripe-band {
    position: absolute;
    left: 0;
    right: 0;
    bottom: 0;
    height: 22px;
    background: var(--navy);
  }

  /* ---------- Back ---------- */
  .card-back {
    left: 620px;
    background: var(--navy-deep);
    display: flex;
    align-items: center;
    justify-content: center;
  }

  .back-wordmark {
    font-family: var(--logo-font);
    font-weight: 400;
    font-size: 26px;
    letter-spacing: 0.6px;
    color: var(--paper);
    white-space: nowrap;
  }
</style>
</head>
<body>

  <section class="card card-front" aria-label="Business card front">
    <div class="front-wordmark">KV Holding Group LLC</div>

    <address class="company-address">
      418 East Marlow Avenue, Suite 7B<br>
      Chicago, Illinois 60617<br>
      facsimile 312-555-0188
    </address>

    <div class="contact-divider">
      <span class="rule rule-left"></span>
      <span class="contact-heading">Contact Details</span>
      <span class="rule rule-right"></span>
    </div>

    <div class="people">
      <div class="person">
        Dorian P. Kell, CPA MST<br>
        Principal<br>
        ofc 312-555-0142<br>
        mobile 312-555-0167<br>
        dorianpkell@kvholdinggroup.example
      </div>
      <div class="person">
        Marcus T. Brenholt, CPA MST<br>
        Principal<br>
        marcustbrenholt@kvholdinggroup.example<br>
        mobile 708-555-0119<br>
        ofc 312-555-0142
      </div>
      <div class="person">
        Nigel F Carrow<br>
        Principal<br>
        ofc 312-555-0142<br>
        nigelfcarrow@kvholdinggroup.example
      </div>
    </div>

    <p class="website">Visit our Website: <a href="#">www.kvholdinggroup.example</a></p>

    <div class="stripe-band" role="img" aria-label="Navy band with white diagonal stripes along the bottom edge"></div>
  </section>

  <section class="card card-back" aria-label="Business card back">
    <div class="back-wordmark">KV Holding Group LLC</div>
  </section>

</body>
</html>
```